Independence Day Graphics for Sale

I want to create 10 social media graphics (new Pictora size 4:5 (1080 x 1350 pixels) focusing on our July 4th Sale Graphics, using any of the pics attached. Use the attached pics, NO RANDOM STOCK PHOTOGRAPHY. For the color scheme of the graphics, they should all be complementary to the product colors in the photos.
You can add any of the photos attached but none are required. You can do some of the graphics in all text. I mainly need BOLD text that says one of the headlines (10 total) SEE ATTACHED WORD DOCUMENT for the headlines to use.

Target Market(s)

women looking to lose weight

Requirements
Must have
• pics attached and text attached

```html
<!DOCTYPE html>
<html lang="en">
<head>
<meta charset="utf-8">
<title>Independence Day Sale Graphics</title>
<link rel="stylesheet" href="https://fonts.googleapis.com/css2?family=Oswald:wght@300;400;700&display=swap">
<style>
  :root {
    --board: #1b1b1b;
    --magenta: #982a74;
    --plum: #7a3a8c;
    --violet: #6a4c9e;
    --blue: #4b63b0;
    --mist-top: #f4eff5;
    --mist-bottom: #d8cde2;
    --photo-light: #8c6d66;
    --photo-dark: #4f3838;
    --ink: #ffffff;
  }
  * { box-sizing: border-box; margin: 0; padding: 0; }
  html, body { width: 1200px; height: 855px; overflow: hidden; background: var(--board); }
  body { position: relative; font-family: "Oswald", sans-serif; color: var(--ink); }

  .post {
    position: absolute;
    overflow: hidden;
    background: linear-gradient(150deg, var(--magenta) 0%, var(--plum) 40%, var(--blue) 75%, var(--violet) 100%);
    box-shadow: 2px 3px 6px rgba(0,0,0,.6);
  }
  .post--hero { left: 30.5px; top: 100.5px; width: 461.5px; height: 577px;
    background: linear-gradient(170deg, var(--blue) 0%, var(--plum) 35%, var(--magenta) 70%, var(--violet) 100%); }
  .post--tile { width: 200px; height: 250px; }
  .col-1 { left: 531.6px; } .col-2 { left: 747.4px; } .col-3 { left: 965.3px; }
  .row-1 { top: 35.3px; } .row-2 { top: 301.6px; } .row-3 { top: 565.8px; }
  .row-3.col-2 { top: 570px; }

  .photo { position: absolute; border-radius: 4px; }
  .photo--person {
    background: linear-gradient(180deg, var(--photo-dark) 0%, var(--photo-light) 55%, var(--photo-dark) 100%);
  }
  .photo--products {
    background: linear-gradient(180deg, var(--mist-top) 0%, var(--mist-bottom) 100%);
  }

  .line { position: absolute; left: 0; right: 0; text-align: center; line-height: 1; white-space: nowrap; }
  .line--left { text-align: left; right: auto; }
  .bold { font-weight: 700; }
  .light { font-weight: 300; }
</style>
</head>
<body>

<section class="post post--hero">
  <div class="photo photo--person" style="left:240px;top:26px;width:206px;height:410px" role="img" aria-label="Smiling woman in a white cropped sweater pointing down at supplement bottles"></div>
  <div class="photo photo--products" style="left:240px;top:446px;width:206px;height:100px" role="img" aria-label="Three supplement bottles on a marble kitchen counter"></div>
  <div class="line bold" style="left:10px;width:235px;right:auto;top:76px;font-size:44px">HISTORIC</div>
  <div class="line bold" style="left:10px;width:235px;right:auto;top:124px;font-size:44px">4TH OF JULY</div>
  <div class="line bold" style="left:10px;width:235px;right:auto;top:168px;font-size:66px">SALE!</div>
  <div class="line light" style="left:10px;width:235px;right:auto;top:255px;font-size:80px">25%</div>
  <div class="line light" style="left:10px;width:235px;right:auto;top:328px;font-size:80px">OFF</div>
  <div class="line light" style="left:10px;width:235px;right:auto;top:410px;font-size:34px">OF EVERYTHING</div>
</section>

<section class="post post--tile col-1 row-1">
  <div class="line bold" style="top:15px;font-size:33px">JULY 4TH</div>
  <div class="line bold" style="top:49px;font-size:26px">MEGA SALE!</div>
  <div class="line light" style="top:84px;font-size:33px">25% OFF</div>
  <div class="line light" style="top:114px;font-size:24px">EVERYTHING</div>
  <div class="photo photo--products" style="left:10px;top:154px;width:180px;height:80px" role="img" aria-label="Four white supplement bottles in a row"></div>
</section>

<section class="post post--tile col-2 row-1">
  <div class="line bold" style="top:20px;font-size:27px">BIGGEST 4TH</div>
  <div class="line bold" style="top:45px;font-size:27px">OF JULY SALE</div>
  <div class="photo photo--products" style="left:10px;top:84px;width:180px;height:82px" role="img" aria-label="Four supplement bottles on a white surface"></div>
  <div class="line light" style="top:181px;font-size:33px">25% OFF</div>
  <div class="line light" style="top:211px;font-size:24px">SITEWIDE</div>
</section>

<section class="post post--tile col-3 row-1">
  <div class="photo photo--person" style="left:92px;top:28px;width:100px;height:150px" role="img" aria-label="Smiling woman in a white sweater in a kitchen"></div>
  <div class="photo photo--products" style="left:28px;top:184px;width:164px;height:52px" role="img" aria-label="Counter lined with supplement products"></div>
  <div class="line bold line--left" style="left:7px;top:6px;font-size:18px">MEGA SUMMER BLOWOUT!</div>
  <div class="line light line--left" style="left:12px;top:27px;font-size:24px">25% OFF</div>
  <div class="line light line--left" style="left:12px;top:51px;font-size:16px">EVERYTHING</div>
</section>

<section class="post post--tile col-1 row-2">
  <div class="photo photo--person" style="left:104px;top:8px;width:88px;height:190px" role="img" aria-label="Smiling woman holding a supplement bottle"></div>
  <div class="photo photo--products" style="left:104px;top:204px;width:88px;height:38px" role="img" aria-label="Two supplement bottles on a counter"></div>
  <div class="line bold" style="left:8px;width:95px;right:auto;top:40px;font-size:22px">ONE-TIME</div>
  <div class="line bold" style="left:8px;width:95px;right:auto;top:63px;font-size:36px">ONLY:</div>
  <div class="line light" style="left:8px;width:95px;right:auto;top:102px;font-size:40px">25%</div>
  <div class="line light" style="left:8px;width:95px;right:auto;top:140px;font-size:40px">OFF</div>
  <div class="line light" style="left:8px;width:95px;right:auto;top:183px;font-size:15px">OF EVERYTHING</div>
</section>

<section class="post post--tile col-2 row-2">
  <div class="line bold" style="top:19px;font-size:33px">25% OFF</div>
  <div class="line bold" style="top:50px;font-size:33px">STOCK-UP</div>
  <div class="line bold" style="top:80px;font-size:33px">EVENT:</div>
  <div class="line light" style="top:121px;font-size:28px">25% OFF ALL</div>
  <div class="line light" style="top:145px;font-size:28px">SUPPLEMENTS</div>
  <div class="photo photo--products" style="left:30px;top:184px;width:140px;height:50px" role="img" aria-label="Four supplement bottles"></div>
</section>

<section class="post post--tile col-3 row-2">
  <div class="line bold" style="top:16px;font-size:31px">THE LOWEST</div>
  <div class="line bold" style="top:44px;font-size:31px">PRICES WE'VE</div>
  <div class="line bold" style="top:72px;font-size:31px">EVER OFFERED!</div>
  <div class="line light" style="top:99px;font-size:48px">25% OFF</div>
  <div class="photo photo--products" style="left:20px;top:158px;width:160px;height:72px" role="img" aria-label="Four supplement bottles in soft focus"></div>
</section>

<section class="post post--tile col-1 row-3">
  <div class="line bold" style="top:21px;font-size:28px">OUR BIGGEST</div>
  <div class="line bold" style="top:47px;font-size:28px">DISCOUNT</div>
  <div class="line bold" style="top:73px;font-size:28px">EVER!</div>
  <div class="line light" style="top:108px;font-size:37px">25% OFF</div>
  <div class="line light" style="top:141px;font-size:30px">EVERYTHING</div>
  <div class="photo photo--products" style="left:30px;top:184px;width:140px;height:50px" role="img" aria-label="Four supplement bottles"></div>
</section>

<section class="post post--tile col-2 row-3">
  <div class="line bold" style="top:34px;font-size:33px">DON’T WAIT!</div>
  <div class="line light" style="top:70px;font-size:49px">25% OFF</div>
  <div class="photo photo--products" style="left:96px;top:127px;width:98px;height:50px" role="img" aria-label="Row of supplement bottles in soft focus"></div>
  <div class="line bold line--left" style="left:20px;top:125px;font-size:33px">ENDS</div>
  <div class="line bold line--left" style="left:20px;top:159px;font-size:33px">SOON</div>
</section>

<section class="post post--tile col-3 row-3">
  <div class="line bold" style="top:28px;font-size:33px">LAST CHANCE</div>
  <div class="photo photo--products" style="left:30px;top:79px;width:140px;height:52px" role="img" aria-label="Four supplement bottles"></div>
  <div class="line light" style="top:154px;font-size:40px">25% OFF</div>
  <div class="line light" style="top:197px;font-size:19px">TIME IS RUNNING OUT!</div>
</section>

</body>
</html>
```